Dalton & Vesh Periodontics and Implant Solutions Business Card

We are a specialty dental practice- implants and periodontal surgery. We have just re-designed our logo and are building a new office and would like to re-design our business card. We are looking for something professional with a creative and artsy twist- something to stand out among the rest! Happy Designing!

I have uploaded all versions of our new logo and our current business card. We have 3 locations and 2 doctors.
Updates

Target Market(s)

55+

Industry/Entity Type

Dental

Contact Information for Business Card

Needs Names, logo, locations- professional and artsy!

Colors
0555a3
0592cd
34a7d7
3277b5
85cae6
85acd3
cee9f5
ecf7fb

Requirements
Must have
• our names:
• Gavin T. Dalton D.M.D.
• Marla P. Vesh D.M.D.
• Diplomate of the National Council of Gum Surgery
• Address locations:
• 462 N. Larkspur Avenue Suite 210B Plantation, FL 33324
• Tel: 954-603-2281 Fax: 954-603-2895
• 5174 Hollins Lane #C-3 Boca Raton, FL 33434
• Tel: 561-327-6018 Fax: 561-327-6092
• 381 Northwest 7th Street #412 Miami FL 33131
• Tel: 786-540-3316 Fax: 786-540-3389
Nice to have
• unique look
Should not have
• doesn't need QR like our current card has.

```html
<!DOCTYPE html>
<html lang="en">
<head>
<meta charset="utf-8">
<title>Dalton &amp; Vesh Periodontics and Implant Solutions – Business Card</title>
<link href="https://fonts.googleapis.com/css2?family=Tinos:wght@400;700&display=swap" rel="stylesheet">
<style>
  :root {
    --navy: #0555a3;
    --blue: #0592cd;
    --sky: #34a7d7;
    --steel: #3277b5;
    --light: #85cae6;
    --mist: #cee9f5;
    --ice: #ecf7fb;
    --page: #ecebe8;
    --white: #ffffff;
  }
  * { margin: 0; padding: 0; box-sizing: border-box; }
  html, body { width: 1200px; height: 1118px; overflow: hidden; }
  body {
    background: var(--page);
    font-family: "Tinos", "Times New Roman", serif;
    position: relative;
  }
  .card {
    position: absolute;
    left: 170px;
    width: 860px;
    height: 491px;
    overflow: hidden;
    box-shadow: 0 6px 18px rgba(0,0,0,.12);
  }
  .card-back { top: 50px; background: var(--navy); padding: 14px; }
  .card-front { top: 577px; background: var(--ice); }

  /* back side */
  .back-panel {
    position: relative;
    width: 100%; height: 100%;
    background: var(--light);
    padding: 62px 0 0 220px;
  }
  .back-ring {
    position: absolute; right: 40px; top: -70px;
    width: 220px; height: 220px; border-radius: 50%;
    border: 10px solid rgba(5,85,163,.10);
  }
  .location { margin-bottom: 14px; color: var(--navy); font-weight: 700; font-size: 21px; line-height: 1.25; }
  .line { display: flex; align-items: center; gap: 10px; }
  .line .indent { padding-left: 30px; }
  .icon { width: 20px; height: 20px; flex: none; }

  /* front side */
  .front-art { position: absolute; inset: 0; }
  .front-ring {
    position: absolute; right: 30px; top: -60px;
    width: 200px; height: 200px; border-radius: 50%;
    border: 10px solid rgba(5,85,163,.08);
  }
  .brand {
    position: absolute; left: 44px; top: 118px;
    display: flex; align-items: center; gap: 14px;
  }
  .brand-mark {
    width: 70px; height: 70px; border-radius: 50%;
    border: 6px solid var(--navy);
  }
  .brand-name { color: var(--navy); font-weight: 700; font-size: 30px; line-height: 1.05; }
  .brand-name span { display: block; font-size: 17px; }
  .practice {
    position: absolute; left: 475px; top: 218px; width: 370px;
    color: var(--white); font-weight: 700; font-size: 19px; line-height: 1.4;
    text-align: center;
  }
  .practice .line { justify-content: center; }
  .doctors {
    position: absolute; left: 110px; top: 360px;
    color: var(--navy); font-weight: 700; font-size: 22px; line-height: 1.45;
  }
</style>
</head>
<body>

<svg width="0" height="0" style="position:absolute">
  <defs>
    <symbol id="i-pin" viewBox="0 0 20 20">
      <circle cx="10" cy="10" r="10" fill="#0555a3"/>
      <path d="M10 4.5a3.6 3.6 0 0 0-3.6 3.6c0 2.7 3.6 7 3.6 7s3.6-4.3 3.6-7A3.6 3.6 0 0 0 10 4.5zm0 5a1.4 1.4 0 1 1 0-2.8 1.4 1.4 0 0 1 0 2.8z" fill="#fff"/>
    </symbol>
    <symbol id="i-phone" viewBox="0 0 20 20">
      <circle cx="10" cy="10" r="10" fill="#0555a3"/>
      <path d="M7 5l2 2.4-1.1 1.3a7 7 0 0 0 3.4 3.4l1.3-1.1L15 13l-.8 1.6c-4.8.1-8.9-4-8.8-8.8z" fill="#fff"/>
    </symbol>
    <symbol id="i-fax" viewBox="0 0 20 20">
      <circle cx="10" cy="10" r="10" fill="#0555a3"/>
      <rect x="7" y="4.5" width="6" height="4" fill="#fff"/>
      <rect x="5" y="8.5" width="10" height="5" rx="1" fill="#fff"/>
      <rect x="7" y="12" width="6" height="3.5" fill="#fff" stroke="#0555a3" stroke-width=".8"/>
    </symbol>
    <symbol id="i-globe" viewBox="0 0 20 20">
      <circle cx="10" cy="10" r="10" fill="#fff"/>
      <g fill="none" stroke="#0555a3" stroke-width="1.2">
        <circle cx="10" cy="10" r="5"/><ellipse cx="10" cy="10" rx="2.2" ry="5"/><path d="M5 10h10"/>
      </g>
    </symbol>
    <symbol id="i-mail" viewBox="0 0 20 20">
      <circle cx="10" cy="10" r="10" fill="#fff"/>
      <rect x="5" y="6.5" width="10" height="7" fill="none" stroke="#0555a3" stroke-width="1.2"/>
      <path d="M5 6.5l5 4 5-4" fill="none" stroke="#0555a3" stroke-width="1.2"/>
    </symbol>
  </defs>
</svg>

<section class="card card-back" aria-label="Card back: locations">
  <div class="back-panel">
    <div class="back-ring"></div>
    <div class="location">
      <div class="line"><svg class="icon"><use href="#i-pin"/></svg>462 N. Larkspur Avenue Suite 210B</div>
      <div class="line"><span class="indent">Plantation, FL 33324</span></div>
      <div class="line"><svg class="icon"><use href="#i-phone"/></svg>954-603-2281</div>
      <div class="line"><svg class="icon"><use href="#i-fax"/></svg>954-603-2895</div>
    </div>
    <div class="location">
      <div class="line"><svg class="icon"><use href="#i-pin"/></svg>5174 Hollins Lane #C-3</div>
      <div class="line"><span class="indent">Boca Raton, FL 33434</span></div>
      <div class="line"><svg class="icon"><use href="#i-phone"/></svg>561-327-6018</div>
      <div class="line"><svg class="icon"><use href="#i-fax"/></svg>561-327-6092</div>
    </div>
    <div class="location">
      <div class="line"><svg class="icon"><use href="#i-pin"/></svg>381 Northwest 7th Street #412</div>
      <div class="line"><span class="indent">Miami FL 33131</span></div>
      <div class="line"><svg class="icon"><use href="#i-phone"/></svg>786-540-3316</div>
      <div class="line"><svg class="icon"><use href="#i-fax"/></svg>786-540-3389</div>
    </div>
  </div>
</section>

<section class="card card-front" aria-label="Card front">
  <svg class="front-art" viewBox="0 0 860 491" preserveAspectRatio="none">
    <polygon points="0,300 300,220 460,450 460,491 0,491" fill="var(--mist)"/>
    <polygon points="300,220 860,140 860,380 460,450" fill="var(--blue)"/>
  </svg>
  <div class="front-ring"></div>

  <div class="brand">
    <div class="brand-mark"></div>
    <div class="brand-name">DALTON &amp; VESH<span>Periodontics and Implant Solutions</span></div>
  </div>

  <div class="practice">
    <div>Practice Limited to Periodontics and Implant Solutions</div>
    <div>9546032281</div>
    <div class="line"><svg class="icon"><use href="#i-globe"/></svg>www.daltonvesh-perio.com</div>
    <div class="line"><svg class="icon"><use href="#i-mail"/></svg>hello@daltonvesh-perio.com</div>
  </div>

  <div class="doctors">
    <div>Gavin T. Dalton D.M.D.</div>
    <div>Marla P. Vesh D.M.D.</div>
  </div>
</section>

</body>
</html>
```